Brevalon Insurance & Consulting

We need a new business card designed.
Front Side:
Photo on left
Logo on top right
Name, title, company, and contact info aligned on right
Clean spacing with professional hierarchy

Back Side:
Tagline centered near the top:
Real expertise. Practical guidance. Reliable protection.

Coverage types centered below in 2 lines:
General Liability | Workers Comp | Commercial Auto
Property | Inland Marine | Excess Liability | Pollution

```html
<!DOCTYPE html>
<html lang="en">
<head>
<meta charset="utf-8">
<title>Brevalon Insurance &amp; Consulting — Business Card</title>
<link rel="stylesheet" href="https://fonts.googleapis.com/css2?family=Montserrat:wght@300;400;600;700&family=Oswald:wght@500&display=swap">
<style>
  :root {
    --backdrop: #3a3a3c;
    --card-white: #ffffff;
    --card-black: #1f1f1f;
    --ink: #111111;
    --ink-soft: #2b2b2b;
    --rule: #9a9a9a;
    --strip-grey: #cfcfcf;
    --paper-text: #ffffff;
    --photo-top: #d9d4cf;
    --photo-mid: #6b5546;
    --photo-low: #2c2c36;
  }
  * { box-sizing: border-box; margin: 0; padding: 0; }
  html, body { width: 1200px; height: 1200px; overflow: hidden; }
  body {
    background: var(--backdrop);
    font-family: "Montserrat", sans-serif;
    display: flex;
    flex-direction: column;
    align-items: center;
    justify-content: center;
    gap: 40px;
  }
  .card {
    width: 960px;
    height: 540px;
    border-radius: 36px;
    overflow: hidden;
    position: relative;
  }
  .card svg { display: block; width: 100%; height: 100%; }

  /* Front */
  .card--front { background: var(--card-white); }
  .brand-name { font-family: "Montserrat", sans-serif; font-weight: 600; fill: var(--ink); }
  .person-name { font-weight: 700; font-size: 34px; fill: var(--ink); letter-spacing: 0.5px; }
  .person-title { font-weight: 300; font-size: 24px; fill: var(--ink-soft); letter-spacing: 1px; }
  .contact-line { font-weight: 400; font-size: 30px; fill: var(--ink); }
  .website { font-weight: 400; font-size: 20px; fill: var(--paper-text); letter-spacing: 0.5px; }

  /* Back */
  .card--back { background: var(--card-black); }
  .brand-name--light { fill: var(--paper-text); }
  .tagline { font-weight: 700; font-size: 30px; fill: var(--paper-text); }
  .coverage { font-family: "Oswald", sans-serif; font-weight: 500; font-size: 27px; fill: var(--paper-text); letter-spacing: 0.5px; text-transform: uppercase; }
</style>
</head>
<body>

  <section class="card card--front" aria-label="Business card front">
    <svg viewBox="0 0 960 540" xmlns="http://www.w3.org/2000/svg">
      <defs>
        <linearGradient id="portrait-tones" x1="0" y1="0" x2="0" y2="1">
          <stop offset="0" stop-color="var(--photo-top)"/>
          <stop offset="0.3" stop-color="var(--photo-mid)"/>
          <stop offset="1" stop-color="var(--photo-low)"/>
        </linearGradient>
      </defs>

      <rect class="portrait" x="610" y="24" width="300" height="416" rx="40" fill="url(#portrait-tones)" role="img" aria-label="Portrait photo of the agency principal in a dark polka-dot dress"/>

      <path class="band-strip" d="M0 490 H470 C530 490 530 420 600 420 H960 V540 H0 Z" fill="var(--strip-grey)"/>
      <path class="band" d="M0 512 H480 C545 512 545 440 615 440 H960 V540 H0 Z" fill="var(--card-black)"/>
      <text class="website" x="930" y="500" text-anchor="end">www.BrevalonInsurance.com</text>

      <g class="brand">
        <circle cx="72" cy="92" r="14" fill="var(--ink)"/>
        <text class="brand-name" x="98" y="102" font-size="30">Brevalon Insurance &amp; Consulting</text>
      </g>

      <line x1="60" y1="236" x2="560" y2="236" stroke="var(--rule)" stroke-width="1.5"/>
      <text class="person-name" x="60" y="290">MARISOL VEGA</text>
      <text class="person-title" x="60" y="324">AGENCY PRINCIPAL</text>
      <line x1="60" y1="350" x2="560" y2="350" stroke="var(--rule)" stroke-width="1.5"/>

      <g class="contact">
        <path class="icon-phone" d="M68 382 c3-3 6-3 8 0 l5 6 c2 2 1 5-1 6 l-3 2 c2 5 6 9 11 11 l2-3 c1-2 4-3 6-1 l6 5 c3 2 3 5 0 8 l-3 3 c-10 4-33-19-35-33 z" fill="var(--ink)"/>
        <text class="contact-line" x="112" y="406">(503) 555-0142</text>
        <g class="icon-mail" fill="none" stroke="var(--ink)" stroke-width="3">
          <rect x="64" y="432" width="36" height="24" rx="2" fill="var(--ink)"/>
          <path d="M64 433 L82 447 L100 433" stroke="var(--card-white)"/>
        </g>
        <text class="contact-line" x="112" y="456">Admin@BrevalonCo.com</text>
      </g>
    </svg>
  </section>

  <section class="card card--back" aria-label="Business card back">
    <svg viewBox="0 0 960 540" xmlns="http://www.w3.org/2000/svg">
      <g class="brand">
        <circle cx="190" cy="170" r="18" fill="var(--paper-text)"/>
        <text class="brand-name brand-name--light" x="224" y="183" font-size="38">Brevalon Insurance &amp; Consulting</text>
      </g>
      <line x1="150" y1="250" x2="810" y2="250" stroke="var(--rule)" stroke-width="1.5"/>
      <text class="tagline" x="480" y="310" text-anchor="middle">Real expertise. Practical guidance. Reliable protection.</text>
      <line x1="150" y1="340" x2="810" y2="340" stroke="var(--rule)" stroke-width="1.5"/>
      <text class="coverage" x="480" y="392" text-anchor="middle">• General Liability • Workers Comp • Commercial Auto</text>
      <text class="coverage" x="480" y="434" text-anchor="middle">• Property • Inland Marine • Excess Liability • Pollution</text>
    </svg>
  </section>

</body>
</html>
```